Premium Organic Ceremonial Matcha Green Tea - Product Label

Two Label Bag Sizes: 18x30cm and 17x24cm

Be EXTRA Creative.. please message me with any questions and I will respond quickly.

Target Market(s)

Health, Organic, Green Tea Matcha Drinkers

Industry/Entity Type

Product

Requirements
Must have
• Organic Matcha Green Tea
• Try to incorporate geometry in logo into design... not mandatory but preferred for branding.

```html
<!DOCTYPE html>
<html lang="en">
<head>
<meta charset="utf-8">
<title>Organic Matcha Green Tea – Label</title>
<link href="https://fonts.googleapis.com/css2?family=Roboto+Condensed:wght@400;700;800&display=swap" rel="stylesheet">
<style>
  :root {
    --backdrop: #f7e6b4;
    --leaf-green: #7dbb5a;
    --deep-green: #0d6a2e;
    --label-yellow: #f9d56e;
    --burst-yellow: #f4ea1c;
    --field-light: #9fcf3c;
    --field-dark: #2f6a1c;
    --white: #ffffff;
  }
  * { margin: 0; padding: 0; box-sizing: border-box; }
  html, body {
    width: 1200px; height: 742px; overflow: hidden;
    background: var(--backdrop);
    font-family: "Roboto Condensed", "Arial Narrow", sans-serif;
  }
  .label {
    position: absolute; left: 338px; top: 0;
    width: 524px; height: 742px; overflow: hidden;
    background: var(--leaf-green);
  }
  .label-shapes { position: absolute; inset: 0; }
  .field-photo {
    position: absolute; left: 14px; right: 14px; top: 444px; bottom: 0;
    background: linear-gradient(180deg, var(--field-light) 0%, #6aa82a 40%, var(--field-dark) 100%);
  }
  .cup-photo {
    position: absolute; left: 34px; top: 470px; width: 230px; height: 200px;
    border-radius: 50%;
    background: radial-gradient(ellipse at center, #f4f2ee 0%, #dcdad4 70%, rgba(220,218,212,0) 100%);
  }
  .brand {
    position: absolute; left: 0; width: 100%; top: 88px;
    display: flex; justify-content: center; align-items: center; gap: 8px;
  }
  .brand-dot { width: 14px; height: 14px; border-radius: 50%; background: var(--leaf-green); }
  .brand-name { font-size: 22px; font-weight: 700; color: var(--leaf-green); }
  .product-title {
    position: absolute; left: 0; width: 100%; top: 176px;
    text-align: center; color: var(--deep-green); font-weight: 800;
    -webkit-text-stroke: 1.5px var(--white); paint-order: stroke fill;
    text-shadow: 2px 2px 3px rgba(0,0,0,.25); line-height: .86;
  }
  .title-line { display: block; font-size: 96px; letter-spacing: 1px; }
  .title-sub { display: block; font-size: 50px; font-weight: 700; margin-top: 8px; }
  .use-burst { position: absolute; left: 340px; top: 408px; width: 128px; height: 128px; }
  .use-burst svg { position: absolute; inset: 0; }
  .use-list {
    position: absolute; inset: 0; display: flex; flex-direction: column;
    justify-content: center; align-items: center;
    transform: rotate(-16deg);
    color: var(--deep-green); font-weight: 700; font-size: 19px; line-height: 1;
  }
  .net-weight {
    position: absolute; left: 240px; right: 14px; top: 648px; height: 40px;
    background: linear-gradient(90deg, rgba(249,213,110,0) 0%, rgba(249,213,110,.85) 18%);
    display: flex; align-items: center; justify-content: flex-end; padding-right: 12px;
    color: var(--deep-green); font-weight: 700; font-size: 21px;
  }
</style>
</head>
<body>
  <main class="label">
    <svg class="label-shapes" width="524" height="742" viewBox="0 0 524 742">
      <polygon points="14,248 150,56 374,56 510,248 510,742 14,742" fill="var(--label-yellow)" stroke="var(--white)" stroke-width="3"/>
      <circle cx="262" cy="42" r="122" fill="var(--white)" stroke="var(--leaf-green)" stroke-width="5"/>
      <circle cx="262" cy="42" r="129" fill="none" stroke="var(--white)" stroke-width="4"/>
    </svg>

    <div class="field-photo" role="img" aria-label="Photo of green tea plantation rows under a clear sky"></div>
    <div class="cup-photo" role="img" aria-label="Photo of a white cup of frothy matcha latte on a saucer with a lace doily and spoon"></div>

    <div class="brand">
      <span class="brand-dot"></span>
      <span class="brand-name">Verdant Grove</span>
    </div>

    <h1 class="product-title">
      <span class="title-line">ORGANIC</span>
      <span class="title-line">MATCHA</span>
      <span class="title-sub">GREEN TEA</span>
    </h1>

    <div class="use-burst">
      <svg viewBox="-64 -64 128 128" width="128" height="128">
        <polygon fill="var(--burst-yellow)" points="64,0 53.1,14.2 55.4,32 38.9,38.9 32,55.4 14.2,53.1 0,64 -14.2,53.1 -32,55.4 -38.9,38.9 -55.4,32 -53.1,14.2 -64,0 -53.1,-14.2 -55.4,-32 -38.9,-38.9 -32,-55.4 -14.2,-53.1 0,-64 14.2,-53.1 32,-55.4 38.9,-38.9 55.4,-32 53.1,-14.2"/>
      </svg>
      <div class="use-list">
        <span>BAKING</span>
        <span>SMOOTHIES</span>
        <span>LATTE</span>
      </div>
    </div>

    <div class="net-weight">Net weight 4oz (113g)</div>
  </main>
</body>
</html>
```